Elegant and modern body scrub for organic junkies

I need a package design for my new company based out of Austin, Texas. We are focused on cruelty free and all natural and organic products. Our deign needs to be able to have the information we require on it, while still appearing very clean and captivating. Our initial product is a clear skin body scrub, intended for people with problematic skin. Our target market is women and we want to show elegance, without appearing "high end."
Updates

Reason: I want to allot more time for certain designers to submit edits. Last minute proposals have been appealing

Target Market(s)

Women. Organic and holistic minded. Natural beauty lovers.

Industry/Entity Type

Skin Care Product

Font styles to use
Script
Other font styles liked:
• AmericanTypewriter, Beautifulflaws, courier, caviarDreams-bold

Colors
000000
ffc214
ffffff
fece3e
fbee3e

Requirements
Must have
• Must be designed in Adobe Illustrator.
• The photo titled “structure for oz and grams” -That needs to be included at the bottom of 1B. I like the horizontal and vertical bar that separate the two. I want that.
• Color Inspiration - The photo titled “vorna color inspiration” and “color combo inspiration” are the colors I want. BLACK, GOLD, WHITE. I want the label background black and the writing in white with some gold somewhere on it. My logo is going to be a golden elephant.
• The photos titled “I like how clean this looks” and “I also like how clean this looks” - I want 1B to look super clean. I don’t want a lot of information in this box. I want simple and clean. This is where the logo and brand name will go.
• Logo - A golden elephant. I want it to be gold and geometric. There can be dimension like this elephant example on the left of the 1B description. I want the trunk to be facing to the left and the trunk needs to be raised overhead and touching the animal's forehead.
• The photo titled “sideways writing and silver rim” - I want 1C to be written sideways like this. My text will be much more extensive so the font won’t be able to be so big.
Nice to have
• The photo titled “sideways writing and silver rim” - I want 1C to be written sideways like this. My text will be much more extensive so the font won’t be able to be so big. I also REALLY like how this label is rimmed in silver, but I would want gold. This is not mandatory, but I really like this.
• The photo titled “melted honey” - This is another option I really like. The gold that looks like honey dripping on the label is really cool. Not mandatory, but I really liked that. I also like the craft background on this.
• Color Inspiration - The photo titled “color inspiration” and “another color inspiration” is an option I would also like to see. Rather than black, I’d like to see what it would ALSO look like with a navy background. NAVY, GOLD, WHITE, maybe black somewhere.
Should not have
• Colorful patterns or excessive info in section 1B.

```html
<!DOCTYPE html>
<html lang="en">
<head>
<meta charset="utf-8">
<title>Clear Skin Body Scrub Label</title>
<link rel="stylesheet" href="https://fonts.googleapis.com/css2?family=Open+Sans:wght@400;600;700&family=Raleway:wght@300;400&display=swap">
<style>
  :root {
    --label-black: #000000;
    --ink-white: #ffffff;
    --gold-deep: #b8860b;
    --gold: #ffc214;
    --gold-light: #fece3e;
    --gold-pale: #fbee3e;
  }
  * { box-sizing: border-box; margin: 0; padding: 0; }
  html, body { width: 1200px; height: 198px; overflow: hidden; background: var(--ink-white); }
  .label {
    position: relative;
    width: 1200px; height: 198px;
    background: linear-gradient(90deg, var(--gold-deep), var(--gold) 18%, var(--gold-pale) 32%, var(--gold-deep) 50%, var(--gold) 68%, var(--gold-pale) 82%, var(--gold-deep));
    font-family: "Open Sans", Arial, sans-serif;
    color: var(--ink-white);
  }
  .label__body {
    position: absolute; inset: 9px 9px;
    background: var(--label-black);
    overflow: hidden;
  }
  /* Left panel */
  .claims {
    position: absolute; left: 31px; top: 26px;
    width: 336px; height: 60px;
    display: grid; grid-template-columns: 104px 86px 1fr;
    border: 1.5px solid var(--ink-white);
    font-size: 8.5px; line-height: 11px; text-align: center;
  }
  .claims__cell { display: flex; flex-direction: column; justify-content: center; align-items: center; }
  .claims__cell + .claims__cell { border-left: 1.5px solid var(--ink-white); }
  .claims__cell--free { align-items: flex-start; text-align: left; padding-left: 9px; }
  .claims__cell--free span:first-child { display: block; width: 100%; text-align: center; margin-left: -10px; }
  .handmade {
    position: absolute; left: 31px; top: 91px;
    font-family: "Raleway", Arial, sans-serif;
    font-size: 11px; font-weight: 400; letter-spacing: 0.2px;
  }
  .usage {
    position: absolute; left: 31px; top: 109px; width: 336px;
    font-size: 7.4px; line-height: 10px;
  }
  .usage p + p { margin-top: 3px; }
  .usage strong { font-weight: 700; }
  /* Center panel */
  .brand-mark {
    position: absolute; left: 536px; top: 40px;
    display: flex; align-items: center; gap: 8px;
    color: var(--gold); font-size: 20px; font-weight: 600; letter-spacing: 3px;
  }
  .brand-mark__dot { width: 16px; height: 16px; border-radius: 50%; background: var(--gold); }
  .brand-name {
    position: absolute; left: 486px; top: 108px; width: 226px;
    font-family: "Raleway", Arial, sans-serif; font-weight: 300;
    font-size: 25px; letter-spacing: 7.5px; text-align: center;
  }
  .net-weight {
    position: absolute; left: 486px; top: 138px; width: 226px; height: 34px;
    border-top: 1.2px solid var(--ink-white);
    font-family: "Raleway", Arial, sans-serif; font-size: 12px;
  }
  .net-weight__divider { position: absolute; left: 113px; top: 0; width: 1.2px; height: 28px; background: var(--ink-white); }
  .net-weight__variant { position: absolute; left: 24px; top: 11px; letter-spacing: 0.5px; }
  .net-weight__mass { position: absolute; left: 158px; top: 11px; }
  /* Right panel: reads bottom to top, columns run left to right */
  .details {
    position: absolute; left: 810px; top: 176px;
    width: 172px; height: 350px;
    transform-origin: top left;
    transform: rotate(-90deg);
    font-family: "Raleway", Arial, sans-serif;
    font-size: 6.6px; line-height: 8.4px;
  }
  .details__title {
    font-weight: 400;
    font-size: 13px; line-height: 16px; letter-spacing: 0.3px;
    margin-bottom: 2px;
  }
  .details__tagline { margin-bottom: 10px; }
  .details__copy { margin-bottom: 10px; }
</style>
</head>
<body>
<div class="label">
  <div class="label__body">
    <div class="claims">
      <div class="claims__cell"><span>Cruelty Free</span><span>Never Tested on Animals</span></div>
      <div class="claims__cell"><span>Organic</span><span>Ingredients</span></div>
      <div class="claims__cell claims__cell--free"><span>FREE OF:</span><span>Parabens, Synthetics, Fragrance,</span><span>GMOs, or any other fakeness.</span></div>
    </div>
    <h2 class="handmade">Handmade in small batches with Love</h2>
    <div class="usage">
      <p><strong>Directions:</strong> Shake well before use. Gently massage scrub in circular motions over wet skin (not face). Pay special attention to rough or dry patches. After use, a residual layer of oil will remain on skin. Rinse thoroughly and pat dry with towel. Skin will feel elegantly soft and nourished. Avoid use on freshly shaven or broken skin.</p>
      <p><strong>Caution:</strong> Oils in product may leave shower or tub surfaces slippery. Not intended for facial use. Essential oils or use on freshly shaven skin may cause skin irritation. External use only.</p>
    </div>

    <div class="brand-mark"><span class="brand-mark__dot"></span><span>VORNA</span></div>
    <h1 class="brand-name">BRANDNAME</h1>
    <div class="net-weight">
      <span class="net-weight__variant">FRESH</span>
      <span class="net-weight__divider"></span>
      <span class="net-weight__mass">260g</span>
    </div>

    <div class="details">
      <h3 class="details__title">CLEAR SKIN BODY SCRUB</h3>
      <p class="details__tagline">Made with naturally derived ingredients only.</p>
      <p class="details__copy">The combination of ingredients in this loved scrub works to gently buff away dull, rough skin while nourishing oils soften and calm. Dead Sea salt is known for its mineral content and helps clarify pores, supporting a clearer looking complexion.</p>
      <p class="details__copy">Pink salt is easily dissolved into the skin, gently exfoliating and purifying the pores while the natural oils help improve the texture, tone and appearance of the skin.</p>
      <p class="details__copy">This loving essential oil blend was chosen to help refresh the skin by removing excess oil and clearing congested areas. Tea tree and lavender have long been valued for soothing blemish prone skin, while rosemary and frankincense support a calm, balanced and even looking complexion.</p>
      <p class="details__copy">Each of these ingredients plays an essential role in this product, working together to leave skin feeling refreshed, smooth and clean. Use this scrub regularly to receive the best results.</p>
      <p class="details__copy">Ingredients: Dead Sea Salt, Pink Himalayan Salt, Coconut Oil, Argan Oil, Jojoba Oil, Almond Oil, Lavender EO, Tea Tree EO, Geranium EO, Cedarwood EO, Frankincense EO, Rosemary EO.</p>
    </div>
  </div>
</div>
</body>
</html>
```